App Design Project

We are building an app and looking for design help on an existing template. We will also need a style guide. For more information, there is a website which outlines the assignment with visuals. Go here:

http://www.brivalora.com/

Industry/Entity Type

Building

```html
<!DOCTYPE html>
<html lang="en">
<head>
<meta charset="utf-8">
<title>Activities – App Screens</title>
<link href="https://fonts.googleapis.com/css2?family=BenchNine:wght@400;700&family=Gudea:wght@400;700&display=swap" rel="stylesheet">
<style>
:root{
  --stage:#e8d6b8;
  --orange:#f0683a;
  --orange-deep:#d9511f;
  --orange-dark:#b8441a;
  --silver-hi:#f4f4f4;
  --silver:#cfcfcf;
  --silver-lo:#9c9c9c;
  --ink:#5a5a5a;
  --cream-hi:#fbf3dd;
  --cream:#f1dcaa;
  --brown-hi:#e07a55;
  --brown:#9c4a2e;
  --brown-lo:#5e2c1e;
  --white:#ffffff;
}
*{box-sizing:border-box;margin:0;padding:0}
html,body{width:1200px;height:879px;overflow:hidden}
body{background:var(--stage);position:relative;font-family:"Gudea",sans-serif}

.screen{position:absolute;top:35px;width:444px;height:789px;overflow:hidden}
.screen--light{left:114px;background:linear-gradient(90deg,#f6e3b4,var(--cream-hi) 45%,#f3e0b0);border-radius:6px;box-shadow:0 4px 12px rgba(0,0,0,.25)}
.screen--dark{left:633px;width:443px;background:linear-gradient(180deg,#e47a55 0%,#c8603c 35%,var(--brown) 75%,#7e3a25 100%);box-shadow:0 4px 12px rgba(0,0,0,.35);border:3px solid #555}

.header{position:absolute;left:0;top:0;width:100%;height:90px;background:linear-gradient(180deg,var(--silver-hi),#dcdcdc 60%,#bdbdbd);border-bottom:2px solid #9a9a9a}
.screen--dark .header{height:86px;background:linear-gradient(180deg,#eaeaea,#bcbcbc 50%,#8e8e8e)}

.round-btn{position:absolute;border-radius:50%;display:flex;align-items:center;justify-content:center;font-family:"BenchNine",sans-serif;color:var(--white);text-transform:uppercase}
.screen--light .round-btn{top:17px;width:56px;height:56px;font-size:17px;background:radial-gradient(circle at 50% 35%,#ff9a73,var(--orange) 55%,var(--orange-dark));border:3px solid #f2f2f2;box-shadow:0 2px 4px rgba(0,0,0,.35)}
.screen--light .round-btn--back{left:24px}
.screen--light .round-btn--sort{left:338px}
.screen--dark .round-btn{top:11px;width:88px;height:88px;font-size:26px;background:radial-gradient(circle at 50% 40%,#e6e6e6,#8a8a8a 55%,#3c3c3c);border:6px solid var(--orange);box-shadow:0 0 0 2px #c44a18,0 3px 6px rgba(0,0,0,.5)}
.screen--dark .round-btn--back{left:14px}
.screen--dark .round-btn--sort{left:341px}

.title{position:absolute;display:flex;align-items:center;justify-content:center;font-family:"BenchNine",sans-serif;text-transform:uppercase;letter-spacing:1px}
.screen--light .title{left:124px;top:15px;width:195px;height:60px;border-radius:30px;font-size:34px;color:var(--white);background:linear-gradient(180deg,#f2f2f2,#bdbdbd);border:2px solid #e0e0e0;box-shadow:inset 0 2px 4px rgba(0,0,0,.25),0 1px 2px rgba(0,0,0,.3);text-shadow:0 1px 2px rgba(0,0,0,.4)}
.screen--dark .title{left:100px;top:14px;width:238px;height:56px;font-size:34px;color:var(--white);background:linear-gradient(180deg,#8a8a8a,#5e5e5e);border-top:2px solid #4a4a4a}

.tray{position:absolute;left:14px;top:90px;width:416px;height:65px;background:linear-gradient(180deg,#7a6a5e,#a8958a);border:3px solid #b08e6a;border-top:none;border-radius:0 0 6px 6px}
.filter{position:absolute;display:flex;align-items:center;justify-content:center;font-family:"BenchNine",sans-serif;font-size:18px;text-transform:uppercase}
.screen--light .filter{top:13px;height:40px;color:#4d4d4d;background:linear-gradient(180deg,#fafafa,#cfcfcf);border-radius:3px;box-shadow:0 2px 3px rgba(0,0,0,.4)}
.screen--light .filter--all{left:16px;width:114px}
.screen--light .filter--people{left:125px;width:115px}
.screen--light .filter--groups{left:261px;width:115px}
.screen--dark .filter{top:110px;height:30px;color:var(--white);background:linear-gradient(180deg,#7a7a7a,#333);border-radius:6px;border-bottom:4px solid #9a9a9a;box-shadow:0 2px 3px rgba(0,0,0,.35)}
.screen--dark .filter--people{border-bottom-color:var(--orange)}
.screen--dark .filter--all{left:38px;width:106px}
.screen--dark .filter--people{left:160px;width:109px}
.screen--dark .filter--groups{left:289px;width:109px}

.panel{position:absolute;left:13px;top:163px;width:416px;height:145px;border-radius:8px;background:rgba(235,125,85,.55);border:1px solid rgba(255,190,160,.6);box-shadow:0 3px 6px rgba(0,0,0,.25)}

.event-card{position:absolute;left:23px;width:396px;height:128px;border-radius:7px;overflow:hidden;border:2px solid #9a9a9a;background:linear-gradient(180deg,#f2f2f2,#cfcfcf);box-shadow:0 3px 6px rgba(0,0,0,.3)}
.event-card--first{top:184px}
.event-card--second{top:334px}
.screen--dark .event-card{left:25px;top:172px;width:392px;height:125px;border:none;border-radius:0}
.event-card__title{position:absolute;left:0;top:0;width:265px;height:35px;padding-left:14px;display:flex;align-items:center;font-family:"BenchNine",sans-serif;font-weight:700;font-size:24px;color:var(--white);text-transform:uppercase;background:linear-gradient(180deg,#f58a5f,var(--orange))}
.event-card__label{position:absolute;left:265px;top:0;width:97px;height:35px;display:flex;align-items:center;justify-content:center;font-family:"BenchNine",sans-serif;font-size:17px;color:var(--white);text-transform:uppercase;background:var(--orange-deep)}
.screen--dark .event-card__label{background:#cf5b30;left:265px}
.event-card__tab{position:absolute;left:362px;top:0;width:34px;height:35px;background:var(--orange)}
.screen--dark .event-card__tab{width:30px;background:linear-gradient(90deg,#f3e3b0,#c9a860)}
.event-card__avatar{position:absolute;left:0;top:35px;width:83px;height:93px;background:linear-gradient(180deg,#f4f4f4,#d6d6d6);border-right:1px solid #b0b0b0}
.avatar-art{position:absolute;left:20px;top:6px;width:44px;height:54px;border-radius:22px 22px 8px 8px;background:linear-gradient(180deg,#c47a3a 0%,#e3b07c 50%,#d0409a 100%)}
.avatar-name{position:absolute;left:0;bottom:8px;width:100%;text-align:center;font-size:15px;color:#4a4a4a}
.event-card__details{position:absolute;left:98px;top:52px;font-size:19px;line-height:23px;color:var(--ink)}
.event-card__expires{position:absolute;left:265px;top:35px;width:97px;height:93px;display:flex;flex-direction:column;align-items:center;justify-content:center;font-family:"BenchNine",sans-serif;font-size:38px;line-height:36px;color:var(--orange);background:linear-gradient(180deg,#dcdcdc,#c0c0c0);border-left:1px solid #9a9a9a}
.screen--dark .event-card__expires{color:#4a4a4a;background:linear-gradient(180deg,#e6e6e6,#bcbcbc)}
.event-card__arrow{position:absolute;left:362px;top:35px;width:34px;height:93px;display:flex;align-items:center;justify-content:center;background:linear-gradient(90deg,var(--orange-deep),#c04f20)}
.screen--dark .event-card__arrow{width:30px;background:linear-gradient(90deg,#8a4a2a,#6a3a22)}

.toolbar{position:absolute;display:flex;align-items:center;justify-content:space-around;padding:0 6px;border-radius:6px;background:linear-gradient(180deg,#f89a72,var(--orange) 50%,var(--orange-deep));border:2px solid #f2c6a6;box-shadow:0 3px 6px rgba(0,0,0,.3)}
.screen--light .toolbar{left:25px;top:671px;width:400px;height:78px}
.screen--dark .toolbar{left:22px;top:686px;width:399px;height:76px}
.tool{width:76px;height:54px;border-radius:50%;display:flex;align-items:center;justify-content:center;background:radial-gradient(ellipse at 50% 30%,#ffffff,#e4e4e4 60%,#b8b8b8);box-shadow:0 2px 4px rgba(0,0,0,.4)}
</style>
</head>
<body>

<section class="screen screen--light" aria-label="Activities screen, light theme">
  <header class="header">
    <div class="round-btn round-btn--back">Back</div>
    <div class="title">Activities</div>
    <div class="round-btn round-btn--sort">Sort</div>
  </header>
  <nav class="tray">
    <div class="filter filter--all">Search All</div>
    <div class="filter filter--people">People</div>
    <div class="filter filter--groups">Groups</div>
  </nav>

  <article class="event-card event-card--first">
    <div class="event-card__title">Midnight Picture Show</div>
    <div class="event-card__label">Expires in</div>
    <div class="event-card__tab"></div>
    <div class="event-card__avatar"><div class="avatar-art" role="img" aria-label="User avatar"></div><div class="avatar-name">Nancy14</div></div>
    <div class="event-card__details">Old Town Cinema<br>October 8, 2012<br>12:00</div>
    <div class="event-card__expires"><span>15H</span><span>39M</span></div>
    <div class="event-card__arrow"><svg width="14" height="22" viewBox="0 0 14 22"><path d="M3 3l8 8-8 8" fill="none" stroke="#fff" stroke-width="3.5"/></svg></div>
  </article>

  <article class="event-card event-card--second">
    <div class="event-card__title">Midnight Picture Show</div>
    <div class="event-card__label">Expires in</div>
    <div class="event-card__tab"></div>
    <div class="event-card__avatar"><div class="avatar-art" role="img" aria-label="User avatar"></div><div class="avatar-name">Nancy14</div></div>
    <div class="event-card__details">Old Town Cinema<br>October 8, 2012<br>12:00</div>
    <div class="event-card__expires"><span>15H</span><span>39M</span></div>
    <div class="event-card__arrow"><svg width="14" height="22" viewBox="0 0 14 22"><path d="M3 3l8 8-8 8" fill="none" stroke="#fff" stroke-width="3.5"/></svg></div>
  </article>

  <footer class="toolbar">
    <div class="tool"><svg width="30" height="30" viewBox="0 0 30 30"><circle cx="12" cy="12" r="8" fill="none" stroke="#c9411a" stroke-width="4"/><path d="M18 18l8 8" stroke="#c9411a" stroke-width="5" stroke-linecap="round"/></svg></div>
    <div class="tool"><svg width="30" height="30" viewBox="0 0 30 30"><path d="M4 3h13v6M4 3v24h18v-7" fill="none" stroke="#c9411a" stroke-width="3"/><path d="M12 20l2-5 11-11 3 3-11 11z" fill="#c9411a"/></svg></div>
    <div class="tool"><svg width="32" height="24" viewBox="0 0 32 24"><rect x="2" y="3" width="28" height="18" fill="#c9411a"/><path d="M2 3l14 11 14-11" fill="none" stroke="#fff" stroke-width="2"/></svg></div>
    <div class="tool"><svg width="30" height="30" viewBox="0 0 30 30"><path d="M8 15L22 6M8 15l14 9" stroke="#c9411a" stroke-width="3"/><circle cx="8" cy="15" r="4.5" fill="#c9411a"/><circle cx="22" cy="6" r="4.5" fill="#c9411a"/><circle cx="22" cy="24" r="4.5" fill="#c9411a"/></svg></div>
  </footer>
</section>

<section class="screen screen--dark" aria-label="Activities screen, dark theme">
  <header class="header">
    <div class="title">Activities</div>
    <div class="round-btn round-btn--back">Back</div>
    <div class="round-btn round-btn--sort">Sort</div>
  </header>
  <div class="filter filter--all">Search All</div>
  <div class="filter filter--people">People</div>
  <div class="filter filter--groups">Groups</div>

  <div class="panel"></div>
  <article class="event-card">
    <div class="event-card__title">Midnight Picture Show</div>
    <div class="event-card__label">Expires in</div>
    <div class="event-card__tab"></div>
    <div class="event-card__avatar"><div class="avatar-art" role="img" aria-label="User avatar"></div><div class="avatar-name">Nancy14</div></div>
    <div class="event-card__details">Old Town Cinema<br>October 8, 2012<br>12:00</div>
    <div class="event-card__expires"><span>15H</span><span>39M</span></div>
    <div class="event-card__arrow"><svg width="14" height="22" viewBox="0 0 14 22"><path d="M3 3l8 8-8 8" fill="none" stroke="#fff" stroke-width="3.5"/></svg></div>
  </article>

  <footer class="toolbar">
    <div class="tool"><svg width="30" height="30" viewBox="0 0 30 30"><circle cx="12" cy="12" r="8" fill="none" stroke="#c9411a" stroke-width="4"/><path d="M18 18l8 8" stroke="#c9411a" stroke-width="5" stroke-linecap="round"/></svg></div>
    <div class="tool"><svg width="30" height="30" viewBox="0 0 30 30"><path d="M4 3h13v6M4 3v24h18v-7" fill="none" stroke="#c9411a" stroke-width="3"/><path d="M12 20l2-5 11-11 3 3-11 11z" fill="#c9411a"/></svg></div>
    <div class="tool"><svg width="32" height="24" viewBox="0 0 32 24"><rect x="2" y="3" width="28" height="18" fill="#c9411a"/><path d="M2 3l14 11 14-11" fill="none" stroke="#fff" stroke-width="2"/></svg></div>
    <div class="tool"><svg width="30" height="30" viewBox="0 0 30 30"><path d="M8 15L22 6M8 15l14 9" stroke="#c9411a" stroke-width="3"/><circle cx="8" cy="15" r="4.5" fill="#c9411a"/><circle cx="22" cy="6" r="4.5" fill="#c9411a"/><circle cx="22" cy="24" r="4.5" fill="#c9411a"/></svg></div>
  </footer>
</section>

</body>
</html>
```